Kestrel Plumbing business card full re design & logo design

Kestrel Plumbing is a Sydney based mechanical plumbing contractor company.
We would like a full redesign with new logo etc which we can take to a future website, uniforms, vehicle sign writing etc.
Blue is my preferred choice of colour but i would be open to see a couple of alternatives thrown in the mix to see how they compare. I am open to see on white cards, black cards etc. Open to many new ideas.
Please see attached original business cards which have been used for the last 5 years.

Target Market(s)

Mechanical services industry.

Industry/Entity Type

Plumbing

Contact Information for Business Card

Dale Fenmore
Director

Mob: 0427 596 418
Email: dale@kestrelplumbing-demo.net.au
PO BOX 782
Ashvale NSW 2190
Lic: 518604k

Logo Text

Kestrel Plumbing

Font styles to use
Sans Serif

Colors
0655a3
3276b5
0792cd
33a6d7
85cae6
000000
333333
474747

Requirements
Must have
• Things that make it very professional and very well presented.
Nice to have
• Same description or very similar to attached uploaded file
Should not have
• Anything that makes it look unprofessional or cartoony.

```html
<!DOCTYPE html>
<html lang="en">
<head>
<meta charset="utf-8">
<title>Kestrel Plumbing – Business Card</title>
<link href="https://fonts.googleapis.com/css2?family=Lato:wght@400;700;900&display=swap" rel="stylesheet">
<style>
  :root {
    --stage: #9b9b9b;
    --card-white: #ffffff;
    --brand-blue: #17608f;
    --name-blue: #1a5f94;
    --text-dark: #474747;
    --rule-light: #d9d9d9;
    --rule-on-blue: rgba(255,255,255,0.25);
    --white: #ffffff;
  }
  * { margin: 0; padding: 0; box-sizing: border-box; }
  html, body {
    width: 1200px; height: 900px; overflow: hidden;
    background: var(--stage);
    font-family: "Lato", Arial, sans-serif;
  }
  .stage { position: relative; width: 1200px; height: 900px; }
  .card {
    position: absolute; top: 306px; height: 272px;
    border-radius: 12px;
    box-shadow: 2px 3px 4px rgba(0,0,0,0.35);
  }
  .card--front { left: 150px; width: 438px; background: var(--card-white); }
  .card--back { left: 609px; width: 441px; background: var(--brand-blue); }

  .brand {
    position: absolute; display: flex; flex-direction: column; align-items: center;
    text-align: center; font-weight: 900; line-height: 1;
  }
  .brand__dot { border-radius: 50%; }
  .brand__name { font-size: 30px; letter-spacing: 0.5px; }
  .brand__name span { display: block; }
  .brand__name span + span { font-size: 17px; letter-spacing: 5.5px; margin-top: 7px; padding-left: 5.5px; }

  .card--front .brand { left: 20px; width: 170px; top: 74px; color: var(--name-blue); }
  .card--front .brand__dot { width: 46px; height: 46px; background: var(--name-blue); margin-bottom: 30px; }

  .card--back .brand { left: 50px; width: 160px; top: 62px; color: var(--white); }
  .card--back .brand__dot { width: 64px; height: 64px; background: var(--white); margin-bottom: 16px; }

  .rule { position: absolute; width: 1px; }
  .card--front .rule { left: 207px; top: 67px; height: 133px; background: var(--rule-light); }
  .card--back .rule { left: 213px; top: 72px; height: 126px; background: var(--rule-on-blue); }

  .contact { position: absolute; left: 225px; top: 78px; color: var(--text-dark); font-size: 13px; white-space: nowrap; }
  .contact__name { font-size: 17.5px; font-weight: 700; color: var(--name-blue); line-height: 1.1; }
  .contact__role { font-size: 13px; line-height: 15px; }
  .contact__lines { list-style: none; margin-top: 7px; }
  .contact__lines li { display: flex; align-items: center; gap: 4px; line-height: 16px; }
  .contact__lines svg { width: 10px; height: 10px; flex: none; }
  .contact__email { font-size: 12.2px; letter-spacing: -0.1px; }
  .contact__address { margin-top: 9px; line-height: 16px; }

  .services {
    position: absolute; left: 236px; top: 77px; list-style: none;
    color: var(--white); font-size: 13.5px;
  }
  .services li { display: flex; align-items: center; gap: 5px; line-height: 19.9px; }
  .services li::before {
    content: ""; width: 7px; height: 7px; border-radius: 50%; background: var(--white);
  }
</style>
</head>
<body>
<main class="stage">
  <section class="card card--front" aria-label="Business card front">
    <div class="brand">
      <div class="brand__dot"></div>
      <p class="brand__name"><span>KESTREL</span><span>PLUMBING</span></p>
    </div>
    <div class="rule"></div>
    <div class="contact">
      <h1 class="contact__name">DALE FENMORE</h1>
      <p class="contact__role">Director</p>
      <ul class="contact__lines">
        <li><svg viewBox="0 0 10 10" aria-hidden="true"><path fill="var(--name-blue)" d="M1 2.5C1 1.5 2 .8 3 1l1 2-1 1c.6 1.3 1.7 2.4 3 3l1-1 2 1c.2 1-.5 2-1.5 2C4 9 1 6 1 2.5z"/></svg>0427 596 418</li>
        <li class="contact__email"><svg viewBox="0 0 10 10" aria-hidden="true"><rect x="0" y="2" width="10" height="6.5" fill="var(--name-blue)"/><path d="M0.5 2.5L5 5.8 9.5 2.5" fill="none" stroke="#fff" stroke-width="0.9"/></svg>dale@kestrelplumbing-demo.net.au</li>
      </ul>
      <p class="contact__address">PO BOX 782 Ashvale<br>NSW 2190</p>
    </div>
  </section>

  <section class="card card--back" aria-label="Business card back">
    <div class="brand">
      <div class="brand__dot"></div>
      <p class="brand__name"><span>KESTREL</span><span>PLUMBING</span></p>
    </div>
    <div class="rule"></div>
    <ul class="services">
      <li>Make Good</li>
      <li>Refurbishment</li>
      <li>Tenancy Fit Out</li>
      <li>Plant Room Works</li>
      <li>Shut Downs</li>
      <li>Change Overs</li>
    </ul>
  </section>
</main>
</body>
</html>
```